New logo and wordpress design for Scholar-pathways.net

We run a website that collates profiles/interviews of individuals who have completed a PhD and moved away from a traditional academix career path into something related. This is often related to the field they studied in, such as publishing, government policy, consulting, teaching and many other things. The website https://scholar-pathways.net aims to give students and researchers ideas about what paths they can take their career on.

We would like to refresh our brand with a new website and logo. Our website is run through wordpress and hence we would need appropriate files and designs to accomodate this.
Our new logo should represent the idea of navigating a career path and exploring the unknown. Up until now it has been a compass in tones of purple and blue. We are happy to keep this motif but would need an updated, more representative logo. We are also happy to get some new ideas if the designer has something they think would fit.
The website itself should have fresh and clean look. We would like a banner at the top with clear links to the various parts of the site. The banner should stay consistent throughout the site.
We would like the main page to have a clean and simple look which places the focus on the profiles and their associated photos.
We would like pictographs to represent the different fields which our profiles fit into and would like to discuss with the winning designer what these would look like exactly. As a starting point we would like pictographs representing STEM (Science, Technology, Engineering, Mathematics) and SHAPE (Social Sciences, Humanities and Arts for People and the Economy).
Updates

We are really looking for something that is clean and professional but embodies our mission to represent all of the major industries which doctoral graduates can go on to work in. Those being, academia (universities), government, industry (private enterprise and companies), and third sector (Charities and think tanks etc.). Any design should cover all of these and not focus just on a big business or similar. It should also represent that we are not purely science focused, but all disciplines and are a broad church in that sense. We are open to various colour schemes and ideas but would like something that gives a professional but approachable feel, it should have elements of Fenwick, but not suggest that we are only open to Fenwick University students or graduates.
Some sites that may be useful are:
https://lumenguild.net/news-resources/projects/research-culture/ - talks about the different areas of employment we are trying to represent
https://www.humstud.fw.ac.uk/ an fenwick internal website that we like the presentation of.

Target Market(s)

Academic researchers with a PhD

Industry/Entity Type

Academic Careers

Colors
0054AA
0677BA
7BADD7
CADEEF
E8F1F8
00AB8E
00BBA5
67D7C9
C6EFE9
E9F9F6
FFF300
FFF600
FEFA6F
FFFEC7
FFFEE8
6B429C
8869AF
B7A5CE
E3DAEB
F3F0F8

Requirements
Must have
• A new logo
Should not have
• The existing logo

```html
<!DOCTYPE html>
<html lang="en">
<head>
<meta charset="utf-8">
<title>Scholar Pathways – Explore Your Options Beyond Academia</title>
<link rel="stylesheet" href="https://fonts.googleapis.com/css2?family=Poppins:wght@300;400;500;600&display=swap">
<style>
:root{
  --purple:#463a87;
  --purple-soft:#6b5fb0;
  --purple-light:#8a86c8;
  --blue-deep:#1c4f95;
  --blue:#2f6fb7;
  --blue-light:#7badd7;
  --ink:#1d1d1f;
  --grey:#6f6f73;
  --white:#ffffff;
  --black:#0f0f10;
}
*{margin:0;padding:0;box-sizing:border-box}
html,body{width:1200px;height:3857px;overflow:hidden}
body{font-family:"Poppins",sans-serif;color:var(--ink);background:var(--white);position:relative}
a{color:inherit;text-decoration:none}

.site-header{position:absolute;top:0;left:0;width:1200px;height:90px;background:var(--white)}
.brand{position:absolute;left:22px;top:22px;font-size:37px;font-weight:500;color:var(--purple);letter-spacing:.2px;display:flex;align-items:center;gap:8px}
.brand-dot{width:10px;height:10px;border-radius:50%;background:var(--purple)}
.main-nav{position:absolute;top:46px;left:464px;display:flex;gap:30px;font-size:13px;font-weight:500;text-transform:uppercase}
.search-box{position:absolute;right:0;top:0;width:144px;height:90px;background:var(--purple);display:flex;align-items:center;justify-content:center}

.hero{position:absolute;top:90px;left:0;width:1200px;height:625px;background:linear-gradient(120deg,#8fb3dc 0%,#3b77bb 40%,#1f5aa2 70%,#6f9fd3 100%)}
.hero-title{position:absolute;left:38px;top:180px;font-size:47px;font-weight:600;line-height:55px;color:var(--white)}
.hero-title .accent{color:var(--purple-light)}
.hero-sub{position:absolute;left:38px;top:308px;font-size:19px;line-height:24px;color:var(--white);width:460px}
.hero-photo{position:absolute;left:591px;top:105px;width:584px;height:493px;border-radius:6px;background:linear-gradient(180deg,rgba(255,255,255,.15),rgba(20,50,110,.35))}

.btn{position:absolute;display:flex;align-items:center;justify-content:center;background:var(--purple);color:var(--white);font-weight:500;font-size:19px;text-transform:uppercase}

.intro{position:absolute;top:810px;left:0;width:1200px;text-align:center}
.intro h2{font-size:24px;font-weight:500;color:var(--purple)}
.intro p{margin:22px auto 0;width:920px;font-size:15.5px;line-height:28px;color:var(--grey);font-weight:300}

.tiles{position:absolute;top:1168px;left:0;width:1200px;height:381px;display:flex}
.tile{position:relative;height:100%;color:var(--white);text-align:center}
.tile.t1{width:396px;background:linear-gradient(135deg,#5f4f9c,#4a3d8c)}
.tile.t2{width:392px;background:linear-gradient(180deg,#5e55a4,#4b3f8e)}
.tile.t3{width:412px;background:linear-gradient(160deg,#6b5ea9,#4f4292)}
.tile h3{position:absolute;left:0;right:0;font-size:26px;font-weight:400}
.tile p{position:absolute;left:30px;right:30px;font-size:12.5px;line-height:20px}
.tile .btn{font-size:19px;height:50px}

.profiles-title{position:absolute;top:1636px;left:0;width:1200px;text-align:center;font-size:38px;font-weight:500;color:var(--purple)}
.card{position:absolute;width:301px;height:492px;background:var(--white);box-shadow:0 20px 60px rgba(0,0,0,.12)}
.card-photo{height:287px}
.card-body{padding:22px 20px 0}
.card-name{font-size:18px;font-weight:500}
.card-role{font-size:9.5px;color:var(--grey);margin:4px 0 10px}
.card-field{font-size:13px;line-height:31px;color:var(--grey)}
.card-field b{font-weight:500;color:var(--ink)}

.disclaimer{position:absolute;top:2983px;left:60px;width:1080px;text-align:center;font-size:18px;line-height:33px}

.join-band{position:absolute;top:3134px;left:0;width:1200px;height:352px;background:linear-gradient(115deg,#6d9fd3 0%,#2d6cb5 45%,#1d4f98 100%)}
.join-band p{position:absolute;top:107px;left:0;width:1200px;text-align:center;font-size:24px;line-height:43px;color:var(--white)}

.site-footer{position:absolute;top:3486px;left:0;width:1200px;height:371px;background:var(--black);color:var(--white);text-align:center}
.footer-brand{position:absolute;top:84px;left:0;width:1200px;font-size:38px;font-weight:500;display:flex;justify-content:center;align-items:center;gap:8px}
.footer-brand .brand-dot{background:var(--white)}
.footer-nav{position:absolute;top:174px;left:0;width:1200px;display:flex;justify-content:center;gap:30px;font-size:13px;font-weight:500}
.social-dot{position:absolute;top:235px;left:584px;width:32px;height:32px;border-radius:50%;background:#1da1f2}
.copyright{position:absolute;top:311px;left:0;width:1200px;font-size:11px}
</style>
</head>
<body>

<header class="site-header">
  <a class="brand" href="https://scholar-pathways.net"><span class="brand-dot"></span>Scholar Pathways</a>
  <nav class="main-nav">
    <a href="#">Home</a><a href="#">Profiles</a><a href="#">Get Involved</a><a href="#">Events</a><a href="#">Resources</a><a href="#">About Us</a>
  </nav>
  <div class="search-box">
    <svg width="36" height="36" viewBox="0 0 36 36" fill="none" stroke="#fff" stroke-width="3"><circle cx="15" cy="15" r="11"/><line x1="23" y1="23" x2="33" y2="33" stroke-linecap="round"/></svg>
  </div>
</header>

<section class="hero">
  <h1 class="hero-title">Explore Your Options<br><span class="accent">Beyond</span> Academia</h1>
  <p class="hero-sub">A collection of profiles of people who have made the transition from academia to industry.</p>
  <a class="btn" href="#" style="left:38px;top:386px;width:228px;height:49px">Get Involved</a>
  <div class="hero-photo" role="img" aria-label="Photo of three smiling professionals seated on wooden stools"></div>
</section>

<section class="intro">
  <h2>Researchers find all sorts of rewarding careers – smart people work everywhere!</h2>
  <p>Such diversity in potential roles can prove challenging when exploring your options. This collection of career profiles enables you to see what others in your position chose to do, why and how they made the move, and what they most enjoy about their job. You will get a feel for their daily activities, workplace culture and work-life balance. Top tip: Look out for authors' insights into which skills developed during or after their PhD proved helpful in getting their job, and performing well there. You'll be encouraged to see how people are building on their research expertise to thrive in newer roles. And don't miss the "employer bio" at the end of each career profile for careers opportunities in each organisation.</p>
</section>

<section class="tiles">
  <div class="tile t1" role="img" aria-label="Purple-tinted photo of a person at work">
    <h3 style="top:128px">Career profiles</h3>
    <p style="top:184px">Explore a collection of profiles from researchers pursuing careers beyond academia.</p>
    <a class="btn" href="#" style="left:71px;top:246px;width:214px">Explore Profiles</a>
  </div>
  <div class="tile t2" role="img" aria-label="Purple-tinted photo of a domed university building">
    <h3 style="top:133px">About Us</h3>
    <p style="top:190px">Explore a collection of profiles from researchers pursuing careers beyond academia.</p>
    <a class="btn" href="#" style="left:77px;top:252px;width:230px">Who We Are</a>
  </div>
  <div class="tile t3" role="img" aria-label="Purple-tinted photo of hands typing on a laptop">
    <h3 style="top:133px">Get Involved</h3>
    <p style="top:190px">Explore a collection of profiles from researchers pursuing careers beyond academia.</p>
    <a class="btn" href="#" style="left:93px;top:252px;width:230px">Find Out How</a>
  </div>
</section>

<h2 class="profiles-title">Recent Profiles</h2>

<article class="card" style="left:85px;top:1778px">
  <div class="card-photo" role="img" aria-label="Portrait of a woman with curly brown hair" style="background:linear-gradient(160deg,#8a7a6c,#3d322c)"></div>
  <div class="card-body"><h3 class="card-name">Marisol Ortega-Vance</h3><p class="card-role">Behavioural Scientist at Brightwell</p>
  <p class="card-field"><b>Career Profiles:</b> PHD</p><p class="card-field"><b>Degree:</b> Psychology</p><p class="card-field"><b>Left academia after:</b> 6+ years postdoc</p><p class="card-field"><b>Sector:</b> Charities</p></div>
</article>
<article class="card" style="left:437px;top:1778px">
  <div class="card-photo" role="img" aria-label="Portrait of a smiling man in a grey jumper" style="background:linear-gradient(160deg,#6b6b68,#2e2e2e)"></div>
  <div class="card-body"><h3 class="card-name">Marisol Ortega-Vance</h3><p class="card-role">Behavioural Scientist at Brightwell</p>
  <p class="card-field"><b>Career Profiles:</b> PHD</p><p class="card-field"><b>Degree:</b> Psychology</p><p class="card-field"><b>Left academia after:</b> 6+ years postdoc</p><p class="card-field"><b>Sector:</b> Charities</p></div>
</article>
<article class="card" style="left:788px;top:1778px">
  <div class="card-photo" role="img" aria-label="Portrait of a smiling woman beside a lake" style="background:linear-gradient(160deg,#4f6b3a,#2c4f6e)"></div>
  <div class="card-body"><h3 class="card-name">Marisol Ortega-Vance</h3><p class="card-role">Behavioural Scientist at Brightwell</p>
  <p class="card-field"><b>Career Profiles:</b> PHD</p><p class="card-field"><b>Degree:</b> Psychology</p><p class="card-field"><b>Left academia after:</b> 6+ years postdoc</p><p class="card-field"><b>Sector:</b> Charities</p></div>
</article>
<article class="card" style="left:84px;top:2316px">
  <div class="card-photo" role="img" aria-label="Portrait of a woman with pink hair in a laboratory" style="background:linear-gradient(160deg,#c9c4bd,#c48a86)"></div>
  <div class="card-body"><h3 class="card-name">Marisol Ortega-Vance</h3><p class="card-role">Behavioural Scientist at Brightwell</p>
  <p class="card-field"><b>Career Profiles:</b> PHD</p><p class="card-field"><b>Degree:</b> Psychology</p><p class="card-field"><b>Left academia after:</b> 6+ years postdoc</p><p class="card-field"><b>Sector:</b> Charities</p></div>
</article>
<article class="card" style="left:435px;top:2316px">
  <div class="card-photo" role="img" aria-label="Portrait of a woman with dark curly hair" style="background:linear-gradient(160deg,#5a6b7a,#1f2530)"></div>
  <div class="card-body"><h3 class="card-name">Marisol Ortega-Vance</h3><p class="card-role">Behavioural Scientist at Brightwell</p>
  <p class="card-field"><b>Career Profiles:</b> PHD</p><p class="card-field"><b>Degree:</b> Psychology</p><p class="card-field"><b>Left academia after:</b> 6+ years postdoc</p><p class="card-field"><b>Sector:</b> Charities</p></div>
</article>
<article class="card" style="left:786px;top:2316px">
  <div class="card-photo" role="img" aria-label="Portrait of a man in a dark shirt in a corridor" style="background:linear-gradient(160deg,#9aa3ad,#2a3340)"></div>
  <div class="card-body"><h3 class="card-name">Marisol Ortega-Vance</h3><p class="card-role">Behavioural Scientist at Brightwell</p>
  <p class="card-field"><b>Career Profiles:</b> PHD</p><p class="card-field"><b>Degree:</b> Psychology</p><p class="card-field"><b>Left academia after:</b> 6+ years postdoc</p><p class="card-field"><b>Sector:</b> Charities</p></div>
</article>

<a class="btn" href="#" style="left:471px;top:2883px;width:229px;height:50px">View All</a>

<p class="disclaimer">The views and opinions expressed in these profiles are those of the individual writer and not of the editorial team, the Careers Service, or other members of the University of Fenwick.</p>

<section class="join-band">
  <p>If you're a DPhil student or member of research staff at the University of Fenwick,<br>you can join the editorial team! Please contact us to find out more.</p>
  <a class="btn" href="#" style="left:485px;top:234px;width:229px;height:50px">Contact Us</a>
</section>

<footer class="site-footer">
  <div class="footer-brand"><span class="brand-dot"></span>Scholar Pathways</div>
  <nav class="footer-nav"><a href="#">PROFILES</a><a href="#">GET INVOLVED</a><a href="#">EVENTS</a><a href="#">RESOURCES</a><a href="#">ABOUT US</a></nav>
  <span class="social-dot" aria-label="Social media"></span>
  <p class="copyright">© 2024 Scholar Pathways – All rights reserved</p>
</footer>

</body>
</html>
```